Yoga/movement guide/teacher for adult yoga practice and kid yoga

What is the positioning or mission statement of your company? to guide individuals in a yoga-based safe and sustainable movement practice applicable to all ages and body types. Currently my focus is working with children in daycare and school settings, but my goal is to expand into private yoga practice for adults, and potentially as part of rented space in studios. I hope to find a way to work with children AND adults (so would love for logo to be appealing to both), but current focus is with children based on need and demand in the community. yoga for children also compliments my backround as a pediatrician/neonatologist, and I greatly miss interacting with children. I also want to emphasize a yoga/movement practice that is focused more on what one feels internally through movement. NOT what one looks like asthetically. I believe in removing all mirrors from yoga/movement practice. It should be an experience of movement/poses/yoga through appropriate cueing and education. It is not about the details of how far the knee should bend, or how high the leg should be. Focusing on foudation first, core, then core engagement and ultimately expression of poses/movements. A focus on strength, stability and mobility, not just flexibility, which is the common perception/association with yoga. I also want individuals to learn to be an advocate of their own health. Through guidance, I hope for individuals to connect with their body so they know themselves so well to be able to advocate for themselves in the modern healthcare world. This internal experience and connection is so essential in a world where modern medicine has become a business and it is all about making a dollar. the connection with patients is lost, and individuals need to learn to empower themselves and through their new found voice to be able to articulate what is wrong.<br/>Does your company have a tagline or slogan that should be included with the logo? "Move With Inner Light"<br/>What do you hope your company can be known for? Accessible yoga for a sustained practice. A guided movement practice where one gains information and knowledge of oneself through a mind/body connection. For one feel good physically with a new awaraness of their internal radiance that exists in all beings. Physical rejuvenation egnites a light and increases energy to flow through the physical body, which ultimately tranlates into works of kindness for others and out in the world. <br/>What color palettes might you prefer? why? love the colors currently chosen<br/>Where will the logo be primarily used? initially business cards, but hopefully future websites, t-shirts, and potentially local magazine adds. Also starting with a small couple of banners for community events in the area. I currently practice as a nomad out of my car :)<br/>Are there any elements you would prefer to see in the logo? Movement. A modern depiction of a human body/figure practicing movement. Hoping to avoid a stereotypical yoga pose per say, just because I want to people to think of it more of a movement practice with yoga roots. Modern yoga. There are elements of breathing and connecting with oneself through the flow of breath and movement, but I do not focus on the meditative/cerebral aspect of the yoga practice. What I teach is almost reaching a meditative state through movement. I personally don't practice, nor resonate with just seated meditation. just not my thing :)<br/>In your opinion, what defines a well-designed logo? curiosity. enough info for individuals to think they know what it means, but want to know more. invokes curiosity, but not too abstract. Reproducible. not too complicated. I want also to invoke a community feel, so a design that appeals to all people within a community. <br/>What is your preference in reference to icons, typography, spokespeople (characters), etc.? modern design. I love the idea of a logo for my purposes, to invoke a sense of movement from within. So not too static. <br/>What words or icons must be included in the logo? movement with yoga roots. <br/>What logos do you like and why? A representation, but not exact. I think some ambiguity is intriguing for others, and also memorable. I want it to be an artistic representation of movement/yoga<br/>What logos do you dislike and why? too busy, too loud. <br/>In your opinion, what is the primary purpose for a logo? association<br/>Who is the primary target audience? (who is most likely to use your services/product?) Children and their parents, but ultimately to expand into teaching adults. I even have aspirations of prenatal and post-natal yoga. Potentially incorporating infants. <br/>Who currently uses your product the most? n/a (working in schools/daycare currently. It is currently all volunteer)<br/>Are you pleased with the range of people your company serves? n/a<br/>Are you looking to expand, modify, or completely change your target audience? or will it remain the same? yes! expand into an adult audience. <br/>How do you plan to focus on your target audience? currently by working through schools and daycares. hopefully ultimately through after school care programs and then offering kid yoga in an existing yoga studio (working on this with Quillbrook in Ridgeland, currently)<br/>What are your main forms of advertising? word of mouth, schools, daycares. Happy kids talking to their parents about the yoga class they took and happy teachers :)<br/>How do most customers find out about your company?<br/>Which gender are you targeting? All genders! However, with kid yoga, often the maternal individual in the child's life is more involved with decision making as far as extracurricular activities

Target Market(s)

individuals and families interested in wellness and feeling great

Contact Information for Business Card

Dana Whitford
Yoga Instructor
RYT-200, RCYT

certified yoga teacher for adults and children

Colors

Requirements
Must have
• "Move With Inner Light"
Nice to have
• logo with same colors

```html
<!DOCTYPE html>
<html lang="en">
<head>
<meta charset="utf-8">
<title>Lumen Studios – Business Card</title>
<link rel="stylesheet" href="https://fonts.googleapis.com/css2?family=Lato:wght@300;400;700&display=swap">
<style>
  :root {
    --backdrop: #2b2925;
    --card: #1f2839;
    --card-light: #253147;
    --sun: #f5d63d;
    --aqua: #4fd8e6;
    --ink: #ffffff;
    --muted: #a6aab3;
  }
  * { box-sizing: border-box; margin: 0; padding: 0; }
  html, body {
    width: 1200px; height: 1200px; overflow: hidden;
    background: var(--backdrop);
    font-family: "Lato", Arial, sans-serif;
  }
  .stage {
    width: 1200px; height: 1200px;
    display: flex; flex-direction: column; align-items: center; justify-content: center;
    gap: 60px;
  }
  .card {
    position: relative;
    width: 900px; height: 514px;
    border-radius: 36px;
    background: radial-gradient(ellipse at 60% 45%, var(--card-light), var(--card) 75%);
    overflow: hidden;
  }
  .brand { display: flex; align-items: center; gap: 22px; }
  .brand-dot { border-radius: 50%; background: var(--sun); flex: none; }
  .brand-name {
    font-weight: 300; color: var(--muted);
    letter-spacing: 1px; white-space: nowrap;
  }
  .brand-tagline {
    font-weight: 300; color: var(--aqua);
    text-transform: uppercase; letter-spacing: 3px; white-space: nowrap;
  }

  /* Front */
  .card-front .brand-block {
    position: absolute; left: 50%; top: 50%;
    transform: translate(-50%, -50%);
    display: flex; flex-direction: column; align-items: flex-start; gap: 14px;
  }
  .card-front .brand-dot { width: 110px; height: 110px; }
  .card-front .brand-name { font-size: 58px; }
  .card-front .brand-tagline { font-size: 15px; padding-left: 132px; }

  /* Back */
  .card-back .brand-block {
    position: absolute; left: 52px; top: 40px;
    display: flex; flex-direction: column; gap: 6px;
  }
  .card-back .brand-dot { width: 80px; height: 80px; }
  .card-back .brand-name { font-size: 40px; }
  .card-back .brand-tagline { font-size: 11px; padding-left: 102px; }

  .divider { position: absolute; inset: 0; }

  .holder-name {
    position: absolute; right: 60px; top: 118px;
    font-size: 44px; font-weight: 400; color: var(--aqua);
    letter-spacing: 1px; text-transform: uppercase; white-space: nowrap;
  }
  .holder-role {
    position: absolute; right: 60px; top: 178px;
    font-size: 20px; color: var(--ink);
  }

  .address {
    position: absolute; right: 60px; top: 244px;
    display: flex; align-items: flex-start; gap: 16px;
    color: var(--ink); font-size: 20px; line-height: 1.45; text-align: right;
  }
  .address svg { margin-top: 6px; }

  .contacts {
    position: absolute; left: 60px; bottom: 30px;
    list-style: none;
    color: var(--ink); font-size: 22px;
  }
  .contacts li { display: flex; align-items: center; gap: 20px; height: 36px; }
  .contacts svg { width: 24px; height: 24px; flex: none; }
</style>
</head>
<body>
<main class="stage">

  <section class="card card-front">
    <div class="brand-block">
      <div class="brand">
        <span class="brand-dot"></span>
        <span class="brand-name">Lumen Studios</span>
      </div>
      <span class="brand-tagline">Move With Inner Light</span>
    </div>
  </section>

  <section class="card card-back">
    <div class="brand-block">
      <div class="brand">
        <span class="brand-dot"></span>
        <span class="brand-name">Lumen Studios</span>
      </div>
      <span class="brand-tagline">Move With Inner Light</span>
    </div>

    <svg class="divider" width="900" height="514" viewBox="0 0 900 514">
      <line x1="60" y1="332" x2="690" y2="190" stroke="var(--sun)" stroke-width="3"/>
    </svg>

    <p class="holder-name">Dana Whitford</p>
    <p class="holder-role">Manager</p>

    <div class="address">
      <svg width="22" height="30" viewBox="0 0 22 30">
        <path d="M11 0C4.9 0 0 4.9 0 11c0 8 11 19 11 19s11-11 11-19C22 4.9 17.1 0 11 0z" fill="var(--sun)"/>
        <circle cx="11" cy="11" r="4" fill="var(--card)"/>
      </svg>
      <p>NY,345 street,your place<br>2nd floor,office no,12<br>Place name,Usa</p>
    </div>

    <ul class="contacts">
      <li>
        <svg viewBox="0 0 24 24"><path d="M6.6 10.8a15 15 0 006.6 6.6l2.2-2.2c.3-.3.7-.4 1-.2 1.1.4 2.3.6 3.6.6.6 0 1 .4 1 1V20c0 .6-.4 1-1 1A17 17 0 013 4c0-.6.4-1 1-1h3.5c.6 0 1 .4 1 1 0 1.3.2 2.5.6 3.6.1.3 0 .7-.2 1z" fill="var(--sun)"/></svg>
        <span>00-11-22-33-44-55</span>
      </li>
      <li>
        <svg viewBox="0 0 24 24"><rect x="6" y="1.5" width="12" height="21" rx="2" fill="none" stroke="var(--sun)" stroke-width="2"/><circle cx="12" cy="19" r="1.2" fill="var(--sun)"/></svg>
        <span>454-232-12</span>
      </li>
      <li>
        <svg viewBox="0 0 24 24"><rect x="1" y="5" width="22" height="14" fill="var(--sun)"/><path d="M1 5l11 8 11-8" fill="none" stroke="var(--card)" stroke-width="1.8"/></svg>
        <span>Yourmail@email.com</span>
      </li>
      <li>
        <svg viewBox="0 0 24 24"><circle cx="12" cy="12" r="10" fill="var(--sun)"/><path d="M2 12h20M12 2c3 3 3 17 0 20M12 2c-3 3-3 17 0 20" fill="none" stroke="var(--card)" stroke-width="1.6"/></svg>
        <span>www.website.com</span>
      </li>
    </ul>
  </section>

</main>
</body>
</html>
```